New website design and logo for BrazeKit.com to help ignite the website sales.

Hi designers,

Brazekit is a new welding brand that is selling welding equipement.

Currently I have around 5 to 10 products. The issue is that the site itself does not do that much of sales. So I have to do something about the seo etc. but that is out of scope for the design.

What is in scope is to comeup with a new logo and website look and feel that is in line with the customers.

men, non professionals, garage, home improvements, perhaps sme ( small mediul entreprice business that want to start in the welding industry.

Products are midrange prices and quality. The look and feel must breath cool stuff, sexy ( women in working cloths carrying welding gloves, other protection gear and weldels)

The wedsite is build in wordpress with the Lumo theme. I am an IT guy myself withhout any creativity in me :( so if you can help me with that that would be great.

Please have a quick look at brazekit.com

Best regards,
Joost

Target Market(s)

non professional welders that do metal work in there garage

Coding

Coded - Design and coding required

Number of Pages Required

3 page

Font styles to use
Sans Serif

Colors
0355a3
ffc214

Requirements
Must have
• I would like to see a new homepage and product page design together with a new logo.
Nice to have
• shop design

```html
<!DOCTYPE html>
<html lang="nl">
<head>
<meta charset="utf-8">
<title>BrazeKit – Lasgereedschap</title>
<link href="https://fonts.googleapis.com/css2?family=Montserrat:ital,wght@0,400;0,500;0,600;0,700;0,800;1,800;1,900&family=Oswald:wght@500&display=swap" rel="stylesheet">
<style>
:root{
  --blue:#0b88c8;
  --blue-dark:#0a74ad;
  --ink:#1e1e1e;
  --text:#333;
  --muted:#666;
  --grey-btn:#6b6b6b;
  --panel-dark:#4a4a4a;
  --footer:#2a2a2a;
  --white:#fff;
  --line:#cfcfcf;
}
*{margin:0;padding:0;box-sizing:border-box}
html,body{width:1200px;height:3976px;overflow:hidden;background:var(--white)}
body{font-family:"Montserrat",sans-serif;color:var(--text);position:relative}
.abs{position:absolute}
.heading{font-family:"Montserrat",sans-serif;font-weight:900;font-style:italic;text-transform:uppercase;letter-spacing:-.5px}
a{color:inherit;text-decoration:none}

/* header */
.site-header{position:absolute;left:0;top:0;width:1200px;height:120px;background:var(--white)}
.brand{position:absolute;left:173px;top:34px;display:flex;align-items:center;gap:12px}
.brand-dot{width:34px;height:34px;border-radius:50%;background:var(--blue)}
.brand-name{font-weight:800;font-size:27px;color:var(--blue);letter-spacing:.5px}
.main-nav{position:absolute;left:469px;top:54px;display:flex;gap:23px;font-size:12.5px;font-weight:500;color:var(--ink)}
.search{position:absolute;left:829px;top:40px;width:198px;height:48px;border:1.5px solid #555;border-radius:4px}
.search span{position:absolute;left:11px;top:15px;font-size:12.5px;color:#555}
.search-btn{position:absolute;right:3px;top:3px;width:38px;height:39px;border-radius:4px;background:var(--blue);display:flex;align-items:center;justify-content:center}

/* hero */
.hero{position:absolute;left:0;top:120px;width:1200px;height:645px;
  background:linear-gradient(180deg,#3a3352 0%,#6b5a86 22%,#a86c72 42%,#c27a4e 58%,#4b3b48 80%,#1d1a24 100%)}
.hero-glow{position:absolute;left:560px;top:0;width:640px;height:645px;background:radial-gradient(ellipse at 50% 45%,rgba(70,80,150,.55),rgba(0,0,0,0) 65%)}
.hero-title{left:173px;top:108px;color:var(--white);font-size:32px;line-height:41px}
.hero-sub{left:173px;top:214px;color:var(--white);font-family:"Oswald",sans-serif;font-weight:500;font-size:18px}
.btn{display:inline-flex;align-items:center;justify-content:center;font-weight:900;font-style:italic;text-transform:uppercase;font-size:14px}
.btn-blue{background:var(--blue);color:var(--white)}
.btn-white{background:var(--white);color:var(--blue)}
.hero-btn{left:172px;top:280px;width:114px;height:56px}
.dots{left:172px;top:391px;display:flex;gap:10px}
.dots i{width:13px;height:13px;border-radius:50%;background:#9a9a9a}
.dots i:first-child{background:var(--white)}

/* intro band */
.intro-band{position:absolute;left:0;top:698px;width:1200px;height:490px}
.intro-title{left:0;width:1200px;top:798px;text-align:center;color:var(--white);font-size:21px;line-height:34px}
.intro-text{left:173px;width:854px;top:890px;text-align:center;color:var(--white);font-size:11.5px;line-height:26px}
.feature-card{position:absolute;top:1062px;width:274px;height:235px;background:var(--white);border:1px solid #8a8a8a}
.shadow{position:absolute;top:1295px;width:274px;height:24px;background:radial-gradient(ellipse at 50% 0%,rgba(0,0,0,.35),rgba(0,0,0,0) 70%)}
.ph{position:absolute}

/* products */
.section-title{left:0;width:1200px;text-align:center;color:var(--ink);font-size:22px}
.lead{left:173px;width:854px;top:1468px;text-align:center;font-size:11.5px;line-height:26px;color:var(--ink)}
.product{position:absolute;top:1590px;width:274px;text-align:center}
.product .ph{position:relative;width:274px;height:235px;border:1px solid #8a8a8a}
.product h3{margin-top:24px;font-size:15.5px;font-weight:500;color:var(--ink);text-transform:uppercase;white-space:nowrap}
.product p{margin-top:12px;font-size:12.5px;color:var(--muted)}
.buy{margin-top:20px;display:flex;justify-content:center;align-items:center;gap:10px}
.price{font-size:18.5px;font-weight:600;color:var(--blue)}
.price.muted{color:var(--muted)}
.cart{height:44px;padding:0 10px;display:flex;align-items:center;font-size:11.5px;font-weight:700;color:var(--white);background:var(--blue)}
.cart.grey{background:var(--grey-btn)}

/* feature rows */
.helmet-row{position:absolute;left:0;top:2066px;width:1200px;height:497px;background:linear-gradient(90deg,#dfe3e8,#eef0f3 50%,#f5f6f8)}
.gloves-row{position:absolute;left:0;top:2563px;width:1200px;height:500px;background:linear-gradient(100deg,#6d6f78 0%,#b7aca0 30%,#d9d4cc 55%,#eeeeee 100%)}
.panel-title{font-size:28px;color:var(--white)}
.panel-text{font-size:11.5px;line-height:26.5px;color:var(--white)}

/* blog */
.blog-card{position:absolute;top:3230px;width:414px;height:241px;border:1px solid #777;background:var(--white)}
.blog-card .ph{left:8px;top:8px;width:173px;height:223px}
.blog-card h4{position:absolute;left:198px;top:36px;font-size:15px;color:var(--ink)}
.blog-card p{position:absolute;left:198px;top:72px;width:202px;font-size:11.5px;line-height:24px;color:var(--text);text-align:justify}
.blog-card .more{position:absolute;left:198px;top:175px;font-size:13px;color:var(--blue)}

/* footer */
.site-footer{position:absolute;left:0;top:3560px;width:1200px;height:416px;background:var(--footer);color:var(--white)}
.footer-brand{left:173px;top:86px;display:flex;align-items:center;gap:12px}
.footer-brand .brand-name{color:var(--white)}
.footer-text{left:173px;top:186px;width:333px;font-size:11.5px;line-height:24.5px;text-align:justify}
.footer-head{font-size:15px;color:var(--white)}
.links{left:591px;top:124px;list-style:none;font-size:12px;line-height:30px}
.contact{left:803px;top:122px;list-style:none;font-size:12px}
.contact li{display:flex;align-items:flex-start;gap:12px;margin-bottom:14px;line-height:22px}
.icon{flex:none;width:30px;height:30px;border-radius:50%;background:var(--blue);display:flex;align-items:center;justify-content:center}
.footer-rule{left:173px;top:323px;width:854px;height:1px;background:#9a9a9a}
.copyright{left:0;width:1200px;top:357px;text-align:center;font-size:12.5px}
</style>
</head>
<body>

<header class="site-header">
  <a class="brand" href="#"><span class="brand-dot"></span><span class="brand-name">BRAZEKIT</span></a>
  <nav class="main-nav"><a href="#">Home</a><a href="#">Products</a><a href="#">Shopping Cart</a><a href="#">My Account</a></nav>
  <div class="search"><span>Search</span>
    <div class="search-btn"><svg width="18" height="18" viewBox="0 0 18 18"><circle cx="7.5" cy="7.5" r="5.5" fill="none" stroke="#fff" stroke-width="2"/><line x1="11.5" y1="11.5" x2="16" y2="16" stroke="#fff" stroke-width="2.4" stroke-linecap="round"/></svg></div>
  </div>
</header>

<section class="hero" role="img" aria-label="Lasser met lashelm boven vonken, met daarachter een stadsskyline bij zonsondergang">
  <div class="hero-glow"></div>
  <h1 class="abs heading hero-title">Eenvoudig staal en<br>aluminium lassen</h1>
  <p class="abs hero-sub">Krijg fantastisch resultaat met gereedschap dat werkt</p>
  <a class="abs btn btn-blue hero-btn" href="#">Shop now</a>
  <div class="abs dots"><i></i><i></i><i></i></div>
</section>

<svg class="intro-band" viewBox="0 0 1200 490" preserveAspectRatio="none"><polygon points="0,66 602,0 1200,42 1200,490 0,490" fill="#0b88c8"/></svg>
<h2 class="abs heading intro-title">Een betere las leggen omdat je handen goed<br>zijn beschermd</h2>
<p class="abs intro-text">Om een goede lassen te kunnen maken is het van belang dat uw handen en onderarmen beschermd zijn tegen hitte, hete druppels, rondv liegende splinters en uv licht.<br>De handschoen moet ruime bescherming bieden tegen de gevaren, maar ook flexibel en comfortabel genoeg om 'het gevoel' tijdens het lassen niet te verliezen.</p>

<div class="feature-card" style="left:173px"><div class="ph" role="img" aria-label="Zwarte leren lashandschoenen" style="left:75px;top:30px;width:124px;height:175px;background:radial-gradient(ellipse,#3d4232,#f4f4f4 72%)"></div></div>
<div class="feature-card" style="left:463px"><div class="ph" role="img" aria-label="Rood lasapparaat" style="left:70px;top:30px;width:134px;height:175px;background:radial-gradient(ellipse,#c8382c,#f4f4f4 72%)"></div></div>
<div class="feature-card" style="left:753px"><div class="ph" role="img" aria-label="Automatische lashelm" style="left:70px;top:30px;width:134px;height:175px;background:radial-gradient(ellipse,#3a3a3e,#f4f4f4 72%)"></div></div>
<div class="shadow" style="left:173px"></div><div class="shadow" style="left:463px"></div><div class="shadow" style="left:753px"></div>

<h2 class="abs heading section-title" style="top:1413px">Twee uitvoeringen</h2>
<p class="abs lead">De BrazeKit lashandschoen is er in 2 uitvoeringen.<br>zwart met gele naden. Deze uitvoering is XXL. De maatvoering is voor een gemiddelde mannen hand. Maar de vrouw kan hem natuurlijk ook gewoon aan alleen valt deze dan iets groter.</p>

<article class="product" style="left:173px">
  <div class="ph" role="img" aria-label="Blauwe lashandschoenen met gele handpalm" style="background:linear-gradient(135deg,#f0f0f0,#c9ccd6 40%,#2a3ea8 70%,#e8e8e8)"></div>
  <h3>Welding gloves blue</h3><p>Full cow split leather back to the cuff.</p>
  <div class="buy"><span class="price">€22,40</span><a class="cart" href="#">IN WINKELMAND</a></div>
</article>
<article class="product" style="left:463px">
  <div class="ph" role="img" aria-label="Kleine zwarte meetdriehoek" style="background:linear-gradient(150deg,#f2f2f2 20%,#2b2b2b 50%,#e8e8e8 80%)"></div>
  <h3>Kleine meetdriehoek | 7 inch</h3><p>Full cow split leather back to the cuff.</p>
  <div class="buy"><span class="price muted">€22,40</span><a class="cart grey" href="#">IN WINKELMAND</a></div>
</article>
<article class="product" style="left:753px">
  <div class="ph" role="img" aria-label="Grote zwarte meetdriehoek" style="background:linear-gradient(150deg,#f2f2f2 20%,#2b2b2b 50%,#e8e8e8 80%)"></div>
  <h3>Grote meetdriehoek | 12 inch</h3><p>Full cow split leather back to the cuff.</p>
  <div class="buy"><span class="price muted">€22,40</span><a class="cart grey" href="#">IN WINKELMAND</a></div>
</article>

<section class="helmet-row">
  <div class="ph" role="img" aria-label="Lashelm met leren handschoenen en laselektroden" style="left:720px;top:60px;width:440px;height:370px;background:radial-gradient(ellipse at 55% 45%,#2a2a2e 0%,#7a3a2c 38%,rgba(238,240,243,0) 70%)"></div>
  <svg class="abs" style="left:114px;top:52px" width="654" height="394" viewBox="0 0 654 394"><polygon points="0,0 654,0 582,394 0,394" fill="#0b88c8"/></svg>
  <h2 class="abs heading panel-title" style="left:173px;top:106px">Welding helmet</h2>
  <div class="abs panel-text" style="left:173px;top:160px;width:506px;text-align:justify">
    <p>Safety comes first with this helmet. The helmet protects you against bright light, heat, sparks and splashes during welding and grinding.</p>
    <p style="margin-top:13px">This helmet has many functions which makes it a professional helmet. The large screen, the advanced automatic filter and solar charging distinguish this helmet from regular mid and low segment helmets.</p>
  </div>
  <a class="abs btn btn-white" href="#" style="left:171px;top:336px;width:116px;height:53px">Shop now</a>
</section>

<section class="gloves-row" role="img" aria-label="Lasser met lashelm en handschoenen aan het werk met een lastoorts">
  <svg class="abs" style="left:437px;top:54px" width="648" height="394" viewBox="0 0 648 394"><polygon points="0,0 648,0 648,394 71,394" fill="#4a4a4a"/></svg>
  <h2 class="abs heading panel-title" style="left:520px;width:504px;top:122px;text-align:right">Welding gloves black</h2>
  <div class="abs panel-text" style="left:518px;top:176px;width:506px;text-align:right">
    <p>Safety comes first with this helmet. The helmet protects you against bright light, heat, sparks and splashes during welding and grinding.</p>
    <p style="margin-top:13px">This helmet has many functions which makes it a professional helmet. The large screen, the advanced automatic filter and solar charging distinguish this helmet from regular mid and low segment helmets.</p>
  </div>
  <a class="abs btn btn-white" href="#" style="left:911px;top:335px;width:116px;height:53px">Shop now</a>
</section>

<h2 class="abs heading section-title" style="top:3150px">Blog posts</h2>
<article class="blog-card" style="left:173px">
  <div class="ph" role="img" aria-label="Lasser in werkkleding aan een stalen balk" style="background:linear-gradient(160deg,#c9c2b4,#6a5a48 55%,#3a2d24)"></div>
  <h4 class="heading">Grote meetdriehoek</h4>
  <p>Afteken gereedschap Meetdrie hoek Brazekit square Lasger eedschap Winkelhaak Dit is de 12" variant.</p>
  <a class="more heading" href="#">Read more</a>
</article>
<article class="blog-card" style="left:613px">
  <div class="ph" role="img" aria-label="Lasser met helm in blauw licht en vonken" style="background:linear-gradient(160deg,#23355c,#3f6aa8 50%,#1a1f2e)"></div>
  <h4 class="heading">Grote meetdriehoek</h4>
  <p>Afteken gereedschap Meetdrie hoek Brazekit square Lasger eedschap Winkelhaak Dit is de 12" variant.</p>
  <a class="more heading" href="#">Read more</a>
</article>

<footer class="site-footer">
  <div class="abs footer-brand"><span class="brand-dot"></span><span class="brand-name">BRAZEKIT</span></div>
  <p class="abs footer-text">Perfect ding voor de hobby en voor de proffesionele lasser. Deze kan natuurlijk ook gebruik worden voor in de houtbouw. Maatvoering op deze haak is metris.</p>
  <h3 class="abs heading footer-head" style="left:591px;top:80px">Quick links</h3>
  <ul class="abs links"><li>Home</li><li>Products</li><li>Customer care</li><li>Informatie</li><li>Bronnen</li></ul>
  <h3 class="abs heading footer-head" style="left:803px;top:80px">Contact us</h3>
  <ul class="abs contact">
    <li><span class="icon"><svg width="14" height="14" viewBox="0 0 14 14"><path d="M3 1l2 3-1.3 1.3a8 8 0 0 0 5 5L10 9l3 2-1 2c-6 0-11-5-11-11z" fill="none" stroke="#fff" stroke-width="1.3"/></svg></span><span style="padding-top:4px">+ 123 456 7890</span></li>
    <li><span class="icon"><svg width="14" height="12" viewBox="0 0 14 12"><rect x="1" y="1" width="12" height="10" rx="1.5" fill="none" stroke="#fff" stroke-width="1.3"/><path d="M1.5 2l5.5 4.5L12.5 2" fill="none" stroke="#fff" stroke-width="1.3"/></svg></span><span style="padding-top:4px">info@brazekit.com</span></li>
    <li><span class="icon"><svg width="12" height="15" viewBox="0 0 12 15"><path d="M6 14s5-5 5-8.5a5 5 0 0 0-10 0C1 9 6 14 6 14z" fill="none" stroke="#fff" stroke-width="1.3"/><circle cx="6" cy="5.5" r="1.8" fill="none" stroke="#fff" stroke-width="1.3"/></svg></span><span style="padding-top:4px">Plot no 123, Down Town st,<br>Dummy Area, UK - 123</span></li>
  </ul>
  <div class="abs footer-rule"></div>
  <p class="abs copyright">Copyrights @ 2021 BrazeKit. All Rights Reserved.</p>
</footer>

</body>
</html>
```